Fair Lend Guide's Mortgage Lantern

For FairLendGuide.org - Creating a sequence of web pages for consumers to understand their mortgage through Mortgage Lantern. There are six pages - want the designer to be willing to design and code those six pages. Most of the pages are very similar.

```html
<!DOCTYPE html>
<html lang="en">
<head>
<meta charset="utf-8">
<title>Mortgage Central – Fair Lend Guide</title>
<link href="https://fonts.googleapis.com/css2?family=Poppins:wght@400;500;600;700&display=swap" rel="stylesheet">
<style>
  :root {
    --header-bg: #f9f9f9;
    --green: #1fb866;
    --green-deep: #0fa552;
    --brand-blue: #1d4ed8;
    --label-blue: #2f5bd0;
    --card-label-bg: #ececec;
    --white: #ffffff;
    --card-top-a: #1f56d6;
    --card-top-b: #1c8f8a;
  }
  * { box-sizing: border-box; margin: 0; padding: 0; }
  html, body { width: 1200px; height: 746px; overflow: hidden; }
  body { font-family: "Poppins", sans-serif; position: relative; background: var(--green); }

  .site-header {
    position: absolute; left: 0; top: 0; width: 1200px; height: 99px;
    background: var(--header-bg);
    display: flex; align-items: center; padding-left: 88px;
  }
  .brand { display: flex; align-items: center; gap: 10px; }
  .brand-mark { width: 26px; height: 26px; background: var(--brand-blue); border-radius: 4px; }
  .brand-name { font-size: 19px; font-weight: 500; color: var(--brand-blue); }

  .hero-backdrop {
    position: absolute; left: 0; top: 99px; width: 1200px; height: 647px;
    background: linear-gradient(135deg, #22bb6a 0%, var(--green) 50%, var(--green-deep) 100%);
  }

  .panel-title {
    position: absolute; left: 230px; top: 264px;
    font-size: 26px; font-weight: 700; color: var(--white); letter-spacing: 0.2px;
  }
  .panel-brand {
    position: absolute; left: 840px; top: 230px; width: 140px;
    display: flex; flex-direction: column; align-items: center; gap: 8px;
  }
  .panel-brand .brand-mark { width: 40px; height: 40px; background: var(--white); border-radius: 5px; }
  .panel-brand .brand-name { color: var(--white); font-size: 17px; white-space: nowrap; }

  .tool-grid {
    position: absolute; left: 230px; top: 320px;
    display: grid; grid-template-columns: repeat(4, 176px);
    column-gap: 12px; row-gap: 19px;
  }
  .tool-card {
    height: 132px; border-radius: 6px; overflow: hidden;
    display: flex; flex-direction: column; background: var(--card-label-bg);
  }
  .tool-card-media {
    height: 82px; position: relative;
    background: linear-gradient(160deg, var(--card-top-a) 0%, #2a63c8 50%, var(--card-top-b) 100%);
    display: flex; align-items: center; justify-content: center;
  }
  .tool-card-media svg { width: 52px; height: 52px; }
  .tool-card-label {
    flex: 1; display: flex; align-items: center; justify-content: center;
    text-align: center; font-size: 12px; font-weight: 600; line-height: 1.4;
    color: var(--label-blue); text-transform: uppercase; padding: 0 6px;
  }
</style>
</head>
<body>
  <header class="site-header">
    <div class="brand">
      <span class="brand-mark"></span>
      <span class="brand-name">Fair Lend Guide</span>
    </div>
  </header>

  <div class="hero-backdrop" role="img" aria-label="Green-tinted photo of a hand holding a credit card over paperwork and a calculator"></div>

  <h1 class="panel-title">MORTGAGE CENTRAL</h1>
  <div class="panel-brand">
    <span class="brand-mark"></span>
    <span class="brand-name">Fair Lend Guide</span>
  </div>

  <main class="tool-grid">
    <a class="tool-card"><div class="tool-card-media" role="img" aria-label="Blue-tinted photo of a desk with financial papers"><svg viewBox="0 0 52 52" fill="none" stroke="#fff" stroke-width="1.8"><circle cx="26" cy="26" r="25"/><path d="M14 36l3-8 15-15a2.5 2.5 0 0 1 4 0l1 1a2.5 2.5 0 0 1 0 4L22 33z" stroke-linejoin="round"/><path d="M30 15l5 5M17 28l5 5"/></svg></div><div class="tool-card-label">Edit Mortgage<br>Profile</div></a>
    <a class="tool-card"><div class="tool-card-media" role="img" aria-label="Blue-tinted photo of a desk with financial papers"><svg viewBox="0 0 52 52" fill="none" stroke="#fff" stroke-width="1.8"><circle cx="26" cy="26" r="25"/><path d="M14 36l3-8 15-15a2.5 2.5 0 0 1 4 0l1 1a2.5 2.5 0 0 1 0 4L22 33z" stroke-linejoin="round"/><path d="M30 15l5 5M17 28l5 5"/></svg></div><div class="tool-card-label">Maximum Mortgage<br>Qualification</div></a>
    <a class="tool-card"><div class="tool-card-media" role="img" aria-label="Blue-tinted photo of a desk with financial papers"><svg viewBox="0 0 52 52" fill="none" stroke="#fff" stroke-width="1.8"><circle cx="26" cy="26" r="25"/><path d="M14 36l3-8 15-15a2.5 2.5 0 0 1 4 0l1 1a2.5 2.5 0 0 1 0 4L22 33z" stroke-linejoin="round"/><path d="M30 15l5 5M17 28l5 5"/></svg></div><div class="tool-card-label">Specific Mortgage<br>Amount</div></a>
    <a class="tool-card"><div class="tool-card-media" role="img" aria-label="Blue-tinted photo of a desk with financial papers"><svg viewBox="0 0 52 52" fill="none" stroke="#fff" stroke-width="1.8"><circle cx="26" cy="26" r="25"/><path d="M14 36l3-8 15-15a2.5 2.5 0 0 1 4 0l1 1a2.5 2.5 0 0 1 0 4L22 33z" stroke-linejoin="round"/><path d="M30 15l5 5M17 28l5 5"/></svg></div><div class="tool-card-label">Specific Mortgage<br>Payment</div></a>
    <a class="tool-card"><div class="tool-card-media" role="img" aria-label="Blue-tinted photo of a desk with financial papers"><svg viewBox="0 0 52 52" fill="none" stroke="#fff" stroke-width="1.8"><circle cx="26" cy="26" r="25"/><path d="M14 36l3-8 15-15a2.5 2.5 0 0 1 4 0l1 1a2.5 2.5 0 0 1 0 4L22 33z" stroke-linejoin="round"/><path d="M30 15l5 5M17 28l5 5"/></svg></div><div class="tool-card-label">Conventional<br>Mortgage Options</div></a>
    <a class="tool-card"><div class="tool-card-media" role="img" aria-label="Blue-tinted photo of a desk with financial papers"><svg viewBox="0 0 52 52" fill="none" stroke="#fff" stroke-width="1.8"><circle cx="26" cy="26" r="25"/><path d="M14 36l3-8 15-15a2.5 2.5 0 0 1 4 0l1 1a2.5 2.5 0 0 1 0 4L22 33z" stroke-linejoin="round"/><path d="M30 15l5 5M17 28l5 5"/></svg></div><div class="tool-card-label">FHA Mortgage<br>Options</div></a>
    <a class="tool-card"><div class="tool-card-media" role="img" aria-label="Blue-tinted photo of a desk with financial papers"><svg viewBox="0 0 52 52" fill="none" stroke="#fff" stroke-width="1.8"><circle cx="26" cy="26" r="25"/><path d="M14 36l3-8 15-15a2.5 2.5 0 0 1 4 0l1 1a2.5 2.5 0 0 1 0 4L22 33z" stroke-linejoin="round"/><path d="M30 15l5 5M17 28l5 5"/></svg></div><div class="tool-card-label">VA Mortgage<br>Options</div></a>
    <a class="tool-card"><div class="tool-card-media" role="img" aria-label="Blue-tinted photo of a desk with financial papers"><svg viewBox="0 0 52 52" fill="none" stroke="#fff" stroke-width="1.8"><circle cx="26" cy="26" r="25"/><path d="M14 36l3-8 15-15a2.5 2.5 0 0 1 4 0l1 1a2.5 2.5 0 0 1 0 4L22 33z" stroke-linejoin="round"/><path d="M30 15l5 5M17 28l5 5"/></svg></div><div class="tool-card-label">USDA Mortgage<br>Options</div></a>
  </main>
</body>
</html>
```